1200mm high x 900mm wide kids fitness poster for gym

I need an a poster designed to promote my kids/teenagers class.

This class is aimed at parents with kids between 10-15.

Design should be friendly and modern

Class is designed for kids that play sport and want to improve their fitness

Industry/Entity Type

Fitness

Font styles to use
Sans Serif

Colors

Designer to choose colors to be used in the design.

Requirements
Must have
• Text:
• Bold Stride teens program (TITLE)
• Improve: Performance, health, fitness, confidence, team mentality (BULLET POINTS)
• They will love our teen program! Contact us now to find out more:
• 1300524196
• enquiries@boldstride.fitness
• www.boldstride.fitness
• Must have friendly image of kids fitness or sport (FUN AND FRIENDLY IMAGE)

```html
<!DOCTYPE html>
<html lang="en">
<head>
<meta charset="utf-8">
<title>Bold Stride Teens Program Poster</title>
<link href="https://fonts.googleapis.com/css2?family=Montserrat:wght@800;900&family=Roboto:ital,wght@0,300;0,400;0,500;0,700;1,700&display=swap" rel="stylesheet">
<style>
  :root {
    --brand-blue: #1d5c9b;
    --deep-navy: #1f4564;
    --footer-blue: #3a6586;
    --sky-light: #d6ecfa;
    --sky-mid: #9fd0f1;
    --hill-blue: #3d6f99;
    --accent-cyan: #3fb0e8;
    --ink: #222222;
    --white: #ffffff;
    --rule-grey: #dcdcdc;
    --page-bg: #eceff2;
  }
  html, body {
    margin: 0;
    padding: 0;
    width: 1200px;
    height: 1200px;
    overflow: hidden;
    background: var(--page-bg);
  }
  .poster {
    position: absolute;
    left: 165px;
    top: 20px;
    width: 870px;
    height: 1160px;
    box-shadow: 0 6px 24px rgba(0,0,0,0.18);
  }
  .poster svg { display: block; width: 100%; height: 100%; }
  .brand-mark { font-family: "Montserrat", sans-serif; font-weight: 800; fill: var(--brand-blue); }
  .title-main { font-family: "Montserrat", sans-serif; font-weight: 900; fill: var(--brand-blue); }
  .title-sub { font-family: "Roboto", sans-serif; font-weight: 300; fill: var(--ink); }
  .improve-word { font-family: "Roboto", sans-serif; font-weight: 300; fill: var(--brand-blue); letter-spacing: 22px; }
  .benefit { font-family: "Roboto", sans-serif; font-weight: 700; font-style: italic; fill: var(--brand-blue); font-size: 31px; }
  .footer-lead { font-family: "Roboto", sans-serif; font-weight: 400; fill: var(--white); }
  .footer-highlight { font-family: "Roboto", sans-serif; font-weight: 700; fill: var(--accent-cyan); }
  .contact-phone { font-family: "Roboto", sans-serif; font-weight: 700; font-style: italic; fill: var(--white); }
  .contact-line { font-family: "Roboto", sans-serif; font-weight: 400; fill: var(--white); }
  .photo-ring { stroke: var(--white); stroke-width: 3; }
</style>
</head>
<body>
<div class="poster">
  <svg viewBox="0 0 962 1282" xmlns="http://www.w3.org/2000/svg">
    <defs>
      <linearGradient id="skyFill" x1="0" y1="0" x2="0" y2="1">
        <stop offset="0" stop-color="#ffffff"/>
        <stop offset="0.25" stop-color="#ffffff"/>
        <stop offset="0.45" stop-color="var(--sky-light)"/>
        <stop offset="1" stop-color="var(--sky-mid)"/>
      </linearGradient>
      <linearGradient id="hillFill" x1="0" y1="0" x2="0" y2="1">
        <stop offset="0" stop-color="#6f9cc4"/>
        <stop offset="1" stop-color="var(--hill-blue)"/>
      </linearGradient>
      <radialGradient id="glow" cx="0.5" cy="0.5" r="0.5">
        <stop offset="0" stop-color="#ffffff" stop-opacity="0.9"/>
        <stop offset="1" stop-color="#ffffff" stop-opacity="0"/>
      </radialGradient>
      <linearGradient id="fieldGreen" x1="0" y1="0" x2="0" y2="1">
        <stop offset="0" stop-color="#b9c9b0"/>
        <stop offset="1" stop-color="#6f9a4c"/>
      </linearGradient>
      <linearGradient id="parkGreen" x1="0" y1="0" x2="1" y2="1">
        <stop offset="0" stop-color="#5f7d46"/>
        <stop offset="1" stop-color="#9aa7a8"/>
      </linearGradient>
      <linearGradient id="gymTone" x1="0" y1="0" x2="1" y2="1">
        <stop offset="0" stop-color="#c8b8b0"/>
        <stop offset="1" stop-color="#4f5a78"/>
      </linearGradient>
      <linearGradient id="boxTone" x1="0" y1="0" x2="1" y2="1">
        <stop offset="0" stop-color="#3a3a3f"/>
        <stop offset="1" stop-color="#c9c2bd"/>
      </linearGradient>
      <linearGradient id="teamTone" x1="0" y1="0" x2="0" y2="1">
        <stop offset="0" stop-color="#a8b3a8"/>
        <stop offset="0.5" stop-color="#c2473f"/>
        <stop offset="1" stop-color="#6c9a4a"/>
      </linearGradient>
      <path id="improveArc" d="M150,645 C190,520 290,410 470,375"/>
    </defs>

    <!-- Backdrop -->
    <rect class="poster-bg" x="0" y="0" width="962" height="1282" fill="url(#skyFill)"/>
    <circle cx="840" cy="400" r="140" fill="url(#glow)"/>
    <circle cx="560" cy="660" r="260" fill="url(#glow)" opacity="0.8"/>

    <!-- Hills -->
    <path class="hills" d="M0,865 C60,880 110,940 170,975 C260,1000 330,1010 420,1020 C560,1030 720,1020 860,990 C910,975 940,965 962,955 L962,1122 L0,1122 Z" fill="url(#hillFill)"/>

    <!-- Runner illustration placeholder -->
    <ellipse role="img" aria-label="Low-poly illustration of a running teen athlete breaking into fragments" cx="690" cy="850" rx="150" ry="240" fill="#8fb5da" opacity="0.55"/>

    <!-- Header band -->
    <polygon class="header-band" points="0,50 412,50 448,110 0,110" fill="var(--brand-blue)"/>
    <polygon class="header-band" points="598,50 962,50 962,110 562,110" fill="var(--brand-blue)"/>
    <rect x="0" y="114" width="450" height="7" fill="var(--rule-grey)"/>
    <rect x="564" y="114" width="398" height="7" fill="var(--rule-grey)"/>
    <text class="brand-mark" x="505" y="93" font-size="17" text-anchor="middle">BOLD STRIDE</text>

    <!-- Title -->
    <text class="title-main" x="504" y="226" font-size="80" text-anchor="middle">BOLD STRIDE</text>
    <text class="title-sub" x="504" y="299" font-size="60" text-anchor="middle">TEENS PROGRAM</text>

    <!-- Improve arc -->
    <path d="M160,1120 C120,880 140,700 230,560 C330,420 520,380 760,412" fill="none" stroke="var(--brand-blue)" stroke-width="4" opacity="0.85"/>
    <text class="improve-word" font-size="44"><textPath href="#improveArc">IMPROVE</textPath></text>

    <!-- Bottom band -->
    <rect class="footer-band" x="0" y="1122" width="962" height="110" fill="var(--deep-navy)"/>
    <rect x="0" y="1232" width="962" height="50" fill="var(--footer-blue)"/>
    <text class="footer-lead" x="56" y="1155" font-size="22">THEY WILL LOVE OUR</text>
    <text class="footer-highlight" x="56" y="1191" font-size="29">TEEN PROGRAM!</text>
    <text class="footer-lead" x="56" y="1221" font-size="17">CONTACT US NOW TO FIND OUT MORE:</text>

    <path d="M632,1124 C614,1126 620,1160 614,1172 C611,1178 606,1178 604,1179 C606,1180 611,1181 614,1187 C620,1199 614,1232 632,1234" fill="none" stroke="var(--white)" stroke-width="2"/>
    <text class="contact-phone" x="642" y="1163" font-size="33">1300524196</text>
    <text class="contact-line" x="642" y="1190" font-size="18">enquiries@boldstride.fitness</text>
    <text class="contact-line" x="642" y="1215" font-size="18">www.boldstride.fitness</text>

    <!-- Photo circles -->
    <circle class="photo-ring" role="img" aria-label="Photo of two teenage footballers contesting the ball" cx="578" cy="523" r="98" fill="url(#fieldGreen)"/>
    <circle class="photo-ring" role="img" aria-label="Photo of a teen doing a yoga pose outdoors" cx="373" cy="591" r="98" fill="url(#parkGreen)"/>
    <circle class="photo-ring" role="img" aria-label="Photo of a teen doing sit-ups in a gym" cx="275" cy="780" r="98" fill="url(#gymTone)"/>
    <circle class="photo-ring" role="img" aria-label="Photo of two teens practising boxing" cx="281" cy="994" r="98" fill="url(#boxTone)"/>
    <circle class="photo-ring" role="img" aria-label="Photo of a youth football team in a huddle" cx="472" cy="1092" r="98" fill="url(#teamTone)"/>

    <!-- Benefits -->
    <text class="benefit" x="668" y="600">PERFORMANCE</text>
    <text class="benefit" x="458" y="688">HEALTH</text>
    <text class="benefit" x="386" y="806">FITNESS</text>
    <text class="benefit" x="380" y="927">CONFIDENCE</text>
    <text class="benefit" x="538" y="1009">TEAM&#160;&#160;MENTALITY</text>
  </svg>
</div>
</body>
</html>
```